Half page (a5) ad for a company

I need a design for an ad for a company to be published in a conference catalogue. Please find enclosed the logo for a company. The company is providing health screening services. Ad should be subtle and minimalistic, i.e. logo in the centre and a phrase saying: "Be in charge of your own health" and the website bluefern.co.uk. Also please find enclosed guidlines for colours and fonts to be used.

```html
<!DOCTYPE html>
<html lang="en">
<head>
<meta charset="utf-8">
<title>Blue Fern – A5 Conference Ad</title>
<link rel="stylesheet" href="https://fonts.googleapis.com/css2?family=Montserrat:wght@400;700&display=swap">
<style>
  :root {
    --canvas-bg: #ffffff;
    --panel-dark: #060707;
    --brand-red: #ec1c24;
    --brand-red-deep: #8a001c;
    --brand-red-mid: #c4141f;
    --text-light: #ffffff;
    --text-dark: #0a0a0a;
  }
  * { margin: 0; padding: 0; box-sizing: border-box; }
  html, body {
    width: 1200px;
    height: 1200px;
    overflow: hidden;
    background: var(--canvas-bg);
  }
  .canvas {
    position: relative;
    width: 1200px;
    height: 1200px;
    background: var(--canvas-bg);
  }
  .ad-page {
    position: absolute;
    left: 216px;
    top: 58px;
    width: 767px;
    height: 1084px;
    display: flex;
    flex-direction: column;
    font-family: "Montserrat", Arial, sans-serif;
  }
  .brand-panel {
    height: 726px;
    background: var(--panel-dark);
    display: flex;
    flex-direction: column;
    align-items: center;
    justify-content: flex-start;
  }
  .brand-mark {
    margin-top: 290px;
    width: 56px;
    height: 56px;
  }
  .brand-name {
    margin-top: 48px;
    color: var(--brand-red);
    font-weight: 400;
    font-size: 78px;
    line-height: 1;
    letter-spacing: 0.5px;
  }
  .message-panel {
    flex: 1;
    background: linear-gradient(90deg, var(--brand-red-deep) 0%, var(--brand-red-mid) 30%, #e01a24 60%, var(--brand-red) 100%);
    display: flex;
    flex-direction: column;
    align-items: center;
  }
  .tagline {
    margin-top: 98px;
    color: var(--text-light);
    font-weight: 700;
    font-size: 40px;
    line-height: 1.1;
    letter-spacing: 0.2px;
    white-space: nowrap;
  }
  .website {
    margin-top: 24px;
    color: var(--text-dark);
    font-weight: 700;
    font-size: 22px;
    line-height: 1;
  }
</style>
</head>
<body>
  <div class="canvas">
    <article class="ad-page">
      <section class="brand-panel">
        <svg class="brand-mark" viewBox="0 0 56 56" aria-hidden="true">
          <circle cx="28" cy="28" r="28" fill="var(--brand-red)"/>
        </svg>
        <h1 class="brand-name">Blue Fern</h1>
      </section>
      <section class="message-panel">
        <p class="tagline">Be in charge of your own health</p>
        <p class="website">bluefern.co.uk</p>
      </section>
    </article>
  </div>
</body>
</html>
```